Medical Breast Thermography Brochure Needed

Looking for a brochure that matches the theme and overall look/feel of our website brightoakcare.com.

http://brightoakcare.com/ourservices/breast-thermography/

I have previously used PixelVenue for logo, business card, and brochure and have been very happy, as soon as designs start being submitted I will switch to guaranteed payment.

I'm looking for a professional, clean, simple, minimalist, bold design.
Colors would ideally be greens and blues, or pink, cool tones, muted colors, or graytones.

See attached word document for content for brochure.

I would like to have the TH1-TH5 images in the Vantora thermo brochure 11.pdf document in the brochure.

Also would like one fold to compare mammogram with breast thermography like in BOCM_thermography_vs_mammography.jpg

I have attached a copy of our prior overall practice brochure to see what type of design I would like.

Feel free to use any stock photos.

```html
<!DOCTYPE html>
<html lang="en">
<head>
<meta charset="utf-8">
<title>Bright Oak Care – Breast Thermography Brochure</title>
<link href="https://fonts.googleapis.com/css2?family=Arvo:wght@400;700&family=PT+Sans:ital,wght@0,400;0,700;1,400&display=swap" rel="stylesheet">
<style>
  :root{
    --stage:#62686c;
    --paper:#ffffff;
    --paper-gray:#ebecec;
    --green:#7aab3a;
    --green-dark:#5f8f25;
    --blue:#1f8fcb;
    --blue-deep:#1d5c7e;
    --ink:#3b3f42;
    --ink-soft:#5d6266;
    --rule:#c9cccd;
  }
  *{box-sizing:border-box;margin:0;padding:0}
  html,body{width:1200px;height:1200px;overflow:hidden;background:var(--stage)}
  body{font-family:"PT Sans",Arial,sans-serif;color:var(--ink)}
  .spread{position:absolute;left:30px;top:160px;width:1140px;height:880px;display:flex;box-shadow:0 10px 30px rgba(0,0,0,.35)}
  .panel{position:relative;width:380px;height:880px;overflow:hidden;background:var(--paper)}
  .panel + .panel{border-left:1px solid #dcdede}

  /* Panel: FAQ */
  .faq{padding:26px 26px 0 26px;font-size:10px;line-height:1.34;font-style:italic;color:var(--ink-soft)}
  .facts{list-style:none;counter-reset:f 3}
  .facts li{counter-increment:f;position:relative;padding-left:12px;margin-bottom:8px}
  .facts li::before{content:counter(f)".";position:absolute;left:0;font-weight:700;color:var(--blue);font-style:normal}
  .faq h3{font-style:normal;color:var(--blue);font-size:11.5px;font-weight:700;line-height:1.2;margin:14px 0 5px}
  .prep{list-style:none;margin-top:5px}
  .prep li{position:relative;padding-left:10px;margin-bottom:4px}
  .prep li::before{content:"";position:absolute;left:0;top:5px;width:4px;height:4px;background:var(--blue-deep)}
  .clinic{margin:14px -26px 0;background:var(--blue);color:#fff;padding:10px 26px 11px}
  .clinic b{font-style:normal}
  .closing{text-align:center;font-style:normal;font-weight:700;color:var(--blue);font-size:11px;margin-top:14px}
  .edge-band{position:absolute;left:0;right:0;bottom:0;height:8px;background:var(--blue)}

  /* Panel: cost */
  .cost{padding:26px 24px 0 26px;font-size:9.2px;line-height:1.32}
  .cost h2{text-align:center;font-size:11px;letter-spacing:1.5px;color:var(--blue-deep);font-weight:700;margin-bottom:8px}
  .fees{width:100%;border:2px solid var(--green);border-radius:8px;border-collapse:separate;border-spacing:0;overflow:hidden;margin:12px 0 22px;font-size:8.6px}
  .fees th{background:var(--green);color:#fff;font-weight:400;font-size:7.6px;padding:4px 3px;line-height:1.1}
  .fees td{padding:5px 4px;border-top:1px solid var(--rule);vertical-align:middle;line-height:1.2}
  .fees td + td{border-left:1px solid var(--rule)}
  .fees td:first-child{text-align:center;width:46px}
  .fees td:last-child{text-align:center;width:52px}
  .help{font-family:"Arvo",Georgia,serif;font-weight:700;text-align:center;font-size:13.5px;line-height:1.3;color:#2b2e30}
  .help-copy{font-style:italic;margin-top:10px;font-size:8.8px}
  .promise{font-family:"Arvo",Georgia,serif;color:var(--ink-soft);font-size:14px;line-height:1.3;margin-top:18px}
  .promise strong{font-weight:400;color:#2b2e30}
  .cta{font-family:"Arvo",Georgia,serif;color:var(--green);font-size:15px;margin-top:22px;letter-spacing:.3px}
  .cta-sub{font-family:"Arvo",Georgia,serif;font-size:12px;color:var(--ink-soft)}
  .contacts{list-style:none;margin-top:14px;font-size:10.5px}
  .contacts li{display:flex;align-items:center;gap:10px;height:22px}
  .contacts svg{width:16px;height:16px;fill:var(--blue-deep)}
  .cost-foot{margin-top:12px}
  .cost-wave{position:absolute;left:0;bottom:0;width:380px;height:70px}

  /* Panel: cover */
  .cover{background:var(--paper-gray)}
  .cover-art{position:absolute;inset:0}
  .brand{position:absolute;left:54px;top:44px;display:flex;align-items:center;gap:12px}
  .brand-dot{width:22px;height:22px;border-radius:50%;background:var(--blue)}
  .brand-name{font-family:"Arvo",Georgia,serif;font-weight:700;font-size:36px;line-height:1;color:var(--blue-deep)}
  .brand-sub{position:absolute;left:90px;top:88px;font-family:"Arvo",Georgia,serif;font-size:11px;letter-spacing:4.5px;color:var(--green-dark)}
  .family-photo{position:absolute;left:14px;top:200px;width:366px;height:430px;background:linear-gradient(160deg,#d9c7b8 0%,#c7b19e 35%,#8da7bd 70%,#b9c8d3 100%)}
  .cover-text{position:absolute;left:0;right:0;top:668px;text-align:center;color:#fff}
  .cover-title{font-family:"Arvo",Georgia,serif;font-size:32px;line-height:1;color:#f4e7e3;letter-spacing:.5px}
  .cover-title2{font-family:"Arvo",Georgia,serif;font-size:24px;margin-top:4px}
  .cover-tag{font-family:"Arvo",Georgia,serif;font-size:15px;color:#eef6dc;margin-top:16px}
  .cover-lede{font-size:14px;line-height:1.25;margin:16px auto 0;width:270px}
  .cover-url{font-size:11px;letter-spacing:4px;margin-top:20px}
</style>
</head>
<body>
<main class="spread">

  <section class="panel faq">
    <ol class="facts">
      <li>Many false negatives occur with mammograms since tumors are frequently located in the upper outer aspects of the breasts where the scans do not reach.</li>
      <li>In Europe, Canada, &amp; Australia healthy breasts are routinely screened with thermography and mammograms are used as a second line of diagnosis.</li>
      <li>For earliest detection and prevention, it is recommended that women receive baseline breast thermography at age 20, every three years between ages 20-30, and annually from age 30.</li>
      <li>Starting breast thermography at any age gives you the safest and earliest detection possible.</li>
    </ol>
    <h3>What are the side effects of Breast Thermography?</h3>
    <p>There are no known short or long-term side effects of breast thermography. It is incredibly safe!</p>
    <h3>How should I prepare for my Breast Thermography appointment?</h3>
    <p>Prior to the test, please adhere to the following:</p>
    <ul class="prep">
      <li>No natural or artificial tanning 5 days prior to your test date</li>
      <li>No breast manipulation prior to the test, including breast self-exams, compression of the breasts, breast stimulation, breast ultrasound, or mammogram for 24h prior to the test</li>
      <li>No fevers for at least 36h prior to the test</li>
      <li>No steam rooms, saunas, heat packs, or cold packs for at least 4 hours prior to the test</li>
      <li>Do not shave your underarms or use skin creams, lotions, deodorants, or powders on your breast before your test</li>
      <li>No coffee, tea, or tobacco two hours before the test</li>
      <li>No restrictive clothing</li>
    </ul>
    <div class="clinic"><b>AT THE CLINIC:</b> Arrive a few minutes early to your appointment. Your body will take time to adjust to the temperature of the clinic. You will be disrobing down to your underwear of choice. You will meet your thermographer who will explain and demonstrate the required views and positions necessary for your exam. Thermal images are then taken of either the whole body or just the regions of interest. A cold "stress" test is performed with this test, which simply involves placing a hand or foot in a cool bowl of water.</div>
    <h3>How long will my appointment last?</h3>
    <p>Your appointment will last 30-60 minutes.</p>
    <h3>When will I get my results?</h3>
    <p>Our board certified Physician evaluates each thermographic image and creates a report. Your comprehensive interpretive report, including images, will be ready to follow up within a 7-14 Business days.</p>
    <p style="margin-top:8px">Our goal is to educate the community to consider thermography when it comes to their health. Some patients ask us to perform a yearly analysis to identify any changes or possible areas of concern. We understand medical testing can be cause of anxiety. We aim to make you experience as pleasant and comfortable as possible.</p>
    <p class="closing">SO WHAT DO YOU THINK?</p>
    <div class="edge-band"></div>
  </section>

  <section class="panel cost">
    <h2>COST</h2>
    <p>Thermography is not yet paid by insurance companies. For this reason, we consider this an alternative service, not requiring a doctor's order and payable at the time of service. Current rates are as follows:</p>
    <table class="fees">
      <thead><tr><th>Procedure Code</th><th>Description</th><th>Standard Fee</th></tr></thead>
      <tbody>
        <tr><td>THBRA</td><td>Thermogram Breast, Annual</td><td>$200.00</td></tr>
        <tr><td>THRO1</td><td>Thermogram 1 Region of Interest (Head, Abdomen, Lower extremities, Upper extremities)</td><td>$180.00</td></tr>
        <tr><td>THROB</td><td>Thermogram 1 Region of Interest With Breasts</td><td>$250.00</td></tr>
        <tr><td>THMHS</td><td>Men's Screen (includes head, neck, thyroid, chest, abdomen, upper and lower back)</td><td>$275.00</td></tr>
        <tr><td>THWHS</td><td>Women's Screen (includes head, neck, thyroid, breast, abdomen/pelvis, upper and lower back)</td><td>$325.00</td></tr>
        <tr><td>THPS</td><td>Thermogram Cervical or Lumbar Study, 3 Sets of images</td><td>$350.00</td></tr>
      </tbody>
    </table>
    <p class="help">Already had Breast Thermography?<br>We need your help!</p>
    <p class="help-copy">If you have already had Breast Thermography at Bright Oak Care we would love it if you could share your feedback about your experience. Your feedback is incredibly valuable and will be able to help thousands of people determine if breast thermography is right for them. Simply send us an email with your feedback today!</p>
    <p class="promise">We provide the <strong>highest quality</strong> imaging and <strong>affordable pricing!</strong></p>
    <p class="cta">CALL TODAY TO SCHEDULE</p>
    <p class="cta-sub">your thermography with our office</p>
    <ul class="contacts">
      <li><svg viewBox="0 0 16 16" aria-hidden="true"><path d="M4 1l3 3-2 2c1 2 3 4 5 5l2-2 3 3-2 2C7 14 2 9 2 3z"/></svg>(555) 014-2290 (Office)</li>
      <li><svg viewBox="0 0 16 16" aria-hidden="true"><path d="M4 1h7l2 2v4h1a1 1 0 011 1v6H1V8a1 1 0 011-1h2zM5 2v5h7V3.5L10.5 2zM3 10v2h10v-2z"/></svg>(555) 014-2291</li>
      <li><svg viewBox="0 0 16 16" aria-hidden="true"><path d="M8 1a7 7 0 100 14A7 7 0 008 1zm0 1.5c.8 0 1.8 1.6 2.1 4H5.9C6.2 4.1 7.2 2.5 8 2.5zM2.6 7.5h2.3v1H2.6zm8.5 0h2.3v1h-2.3zM5.9 9.5h4.2c-.3 2.4-1.3 4-2.1 4s-1.8-1.6-2.1-4z"/></svg>www.brightoakcare.com</li>
      <li><svg viewBox="0 0 16 16" aria-hidden="true"><path d="M8 1l7 6h-2v8H9v-5H7v5H3V7H1z"/></svg>410 Linden Park Rd. Fairview, TX 79000</li>
    </ul>
    <p class="cost-foot">1in8 get breast cancer you don't have to be one of them. Call today to let us help you minimize your breast cancer risk and optimize your health.</p>
    <svg class="cost-wave" viewBox="0 0 380 70" aria-hidden="true">
      <path d="M0 70 Q190 0 380 40 V70Z" fill="#e3e5e6"/>
      <path d="M90 52 Q230 6 380 30" stroke="var(--blue)" stroke-width="5" fill="none"/>
      <rect x="0" y="64" width="380" height="6" fill="var(--blue)"/>
    </svg>
  </section>

  <section class="panel cover">
    <svg class="cover-art" viewBox="0 0 380 880" aria-hidden="true">
      <path d="M60 240 Q200 130 380 120" stroke="var(--green)" stroke-width="2" fill="none"/>
      <path d="M30 300 Q20 520 70 660" stroke="var(--blue)" stroke-width="8" fill="none"/>
    </svg>
    <div class="brand"><span class="brand-dot"></span><span class="brand-name">Bright Oak</span></div>
    <div class="brand-sub">FAMILY MEDICINE</div>
    <div class="family-photo" role="img" aria-label="Photo of a smiling family of four: parents with a young girl and boy riding on their backs"></div>
    <svg class="cover-art" viewBox="0 0 380 880" aria-hidden="true">
      <path d="M0 880 V690 Q190 560 380 640 V880Z" fill="#fff"/>
      <path d="M0 880 V700 Q190 575 380 652 V880Z" fill="var(--green)"/>
    </svg>
    <div class="cover-text">
      <p class="cover-title">BREAST</p>
      <p class="cover-title2">Thermography</p>
      <p class="cover-tag">Safe Screening. Early Detection</p>
      <p class="cover-lede">Now you don't have to wait till your next mammogram to get a window into your breast health!</p>
      <p class="cover-url">WWW.BRIGHTOAKCARE.COM</p>
    </div>
  </section>

</main>
</body>
</html>
```